Billboard Design for Modern Dispensary

Hello!
We need a eye-catching 12' x 24' billboard designed for a very successful, modern cannabis dispensary on the Oregon coast, United States. Because of rules, we cannot have any marijuana leafs or other cannabis related images (flower, joints, smoke, etc). We can use the words "Shop" or "Dispensary" - we cannot use the words "cannabis", "marijuana".

Some ideas we had are 3 words stacked on left or center of billboard - maybe across bottom we have horizontal logo and the following words - “South of bridge in Gull Harbor”
Another idea is to have a small bubble in bottom/top corner with image of our dog (face only) - with some words around it - like "BONUS Shop Dog" or "Cute Shop Dog" or "Best Shop Dog" or "Friendly Staff"

here's some 3 word examples:
ENJOY
YOUR
TRIP

or

FEEL
GOOD
JUST
AHEAD

or

GOOD
VIBES
ONLY

or

GOOD
TIMES
CHILL
VIBES

I have attached our logo. I have also included a stacked logo version (vertical, not horizontal). the formats are .EPS and .PDF - the logos were created in Affinity Design 2.x.

Our website is coralnook.net if you want to see more images, etc about our dispensary.

Artwork Requirements:
The billboard is 12' tall x 25' wide
The artwork needs to be 1”=1’ @ 300dpi
Please add 6” of bleed all around so your total artwork is 13”x26”
Final deliverable should be .Ai file.

Font styles to use
Sans Serif

Colors
0054AA
0677BA
7BADD7
CADEEF
E8F1F8

Requirements
Nice to have
• See the project description - we included some ideas to consider.
Should not have
• No cannabis images, like flower, cannabis leaves, paraphenlia, cartridges, joints, etc.

```html
<!DOCTYPE html>
<html lang="en">
<head>
<meta charset="utf-8">
<title>Coral Nook Billboard</title>
<link rel="stylesheet" href="https://fonts.googleapis.com/css2?family=League+Gothic&family=Noto+Sans:wght@400;700&family=Poppins:wght@400&display=swap">
<style>
  :root {
    --backdrop: #222222;
    --board: #ffffff;
    --ink: #1a1a1a;
    --sky-blue: #4b9fd6;
    --band-blue: #0f77bb;
    --band-dark: #1b1b1b;
    --fur: #b88e57;
  }
  html, body {
    margin: 0;
    padding: 0;
    width: 944px;
    height: 1200px;
    overflow: hidden;
    background: var(--backdrop);
  }
  .canvas {
    position: relative;
    width: 944px;
    height: 1200px;
  }
  .billboard {
    position: absolute;
    left: 42px;
    top: 375px;
    width: 860px;
    height: 451px;
    background: var(--board);
    overflow: hidden;
  }
  .brand {
    position: absolute;
    left: 239px;
    top: 30px;
    display: flex;
    align-items: center;
    gap: 10px;
  }
  .brand-mark {
    width: 104px;
    height: 104px;
    border-radius: 50%;
    border: 6px solid var(--sky-blue);
    box-sizing: border-box;
  }
  .brand-text {
    display: flex;
    flex-direction: column;
  }
  .brand-name {
    font-family: "Poppins", sans-serif;
    font-weight: 400;
    font-size: 46px;
    line-height: 1;
    color: var(--sky-blue);
    letter-spacing: 0.3px;
  }
  .brand-tagline {
    font-family: "Poppins", sans-serif;
    font-size: 16px;
    line-height: 1;
    color: var(--ink);
    margin-top: 6px;
    text-transform: uppercase;
  }
  .headline {
    position: absolute;
    left: 50%;
    top: 152px;
    display: inline-block;
    margin: 0;
    font-family: "League Gothic", sans-serif;
    font-weight: 400;
    font-size: 158px;
    line-height: 1;
    color: var(--ink);
    white-space: nowrap;
    transform: translateX(-50%) scaleX(0.68);
    transform-origin: center;
  }
  .headline .accent { color: var(--sky-blue); }
  .band {
    position: absolute;
    top: 354px;
    height: 68px;
    display: flex;
    align-items: center;
    font-family: "Noto Sans", sans-serif;
    font-weight: 700;
    color: #ffffff;
  }
  .band-phone {
    left: 0;
    width: 434px;
    background: var(--band-blue);
  }
  .band-staff {
    left: 434px;
    width: 426px;
    background: var(--band-dark);
  }
  .phone-icon {
    width: 36px;
    height: 36px;
    margin-left: 32px;
    margin-right: 21px;
  }
  .phone-number {
    font-size: 44px;
    letter-spacing: 0.5px;
  }
  .staff-label {
    font-size: 39px;
    margin-left: 116px;
    letter-spacing: 0.5px;
  }
  .shop-dog {
    position: absolute;
    left: 421px;
    top: 323px;
    width: 114px;
    height: 118px;
    border-radius: 50%;
    border: 4px solid var(--band-dark);
    box-sizing: border-box;
    background: radial-gradient(circle at 50% 45%, #d9b27a 0%, var(--fur) 55%, #5a4a38 100%);
  }
</style>
</head>
<body>
<div class="canvas">
  <section class="billboard">
    <div class="brand">
      <div class="brand-mark"></div>
      <div class="brand-text">
        <span class="brand-name">CORAL NOOK</span>
        <span class="brand-tagline">South of bridge in Gull Harbor</span>
      </div>
    </div>

    <h1 class="headline">BEST <span class="accent">DISPENSARY</span> PERIOD</h1>

    <div class="band band-phone">
      <svg class="phone-icon" viewBox="0 0 24 24" aria-hidden="true">
        <path fill="#ffffff" d="M6.6 10.8c1.4 2.8 3.8 5.1 6.6 6.6l2.2-2.2c.3-.3.7-.4 1-.2 1.1.4 2.300.6 3.6.6.6 0 1 .4 1 1V20c0 .6-.4 1-1 1C10.6 21 3 13.4 3 4c0-.6.4-1 1-1h3.5c.6 0 1 .4 1 1 0 1.3.2 2.5.6 3.6.1.3 0 .7-.2 1l-2.3 2.2z"/>
        <path fill="none" stroke="#ffffff" stroke-width="1.8" stroke-linecap="round" d="M14.5 3.5a6.5 6.5 0 0 1 6 6M14.2 7a3 3 0 0 1 2.8 2.8"/>
      </svg>
      <span class="phone-number">41-555-0142</span>
    </div>

    <div class="band band-staff">
      <span class="staff-label">Friendly Staff</span>
    </div>

    <div class="shop-dog" role="img" aria-label="Round photo of the shop's golden doodle dog"></div>
  </section>
</div>
</body>
</html>
```